Real Estate Investment Opportunity needs a print and web brochure

need a porfessional looking information brochure to present and describe the investment opportunity.
This is an introductory brochure AND a take away brochure from investment meetings.
Ideally it will be easy to amend content and edit after.
Preliminary content is drafted, some photos are available.
Once the layout is completed the brochure will need to be translated into FRENCH (canadian), so it is available in both official languages of Canada. If you are capable of proper translating, that is a plus, but if not - translated text can be provided later
Updates
This assignment could also be done in power point.
Target Market(s)
medium to high net worth individuals
Industry/Entity Type
Investment
Look and feel

```html
<!DOCTYPE html>
<html lang="en">
<head>
<meta charset="utf-8">
<title>Les Résidences Horizon – Investment Brochure</title>
<link rel="stylesheet" href="https://fonts.googleapis.com/css2?family=Cabin:wght@500&family=Arimo:wght@400&display=swap">
<style>
  :root {
    --teal: #3ab0c3;
    --teal-text: #2fb3c8;
    --body-text: #3a3a3a;
    --paper: #ffffff;
    --frame: #9a9a9a;
    --grid-line: rgba(255, 255, 255, 0.85);
    --sky: #a9c9e6;
    --sky-deep: #7fa9d4;
    --stone: #9b7a63;
    --foliage: #2f5a2a;
    --harbour: #8a8678;
    --water: #4d5a56;
  }
  * { margin: 0; padding: 0; box-sizing: border-box; }
  html, body {
    width: 1200px;
    height: 802px;
    overflow: hidden;
    background: var(--paper);
  }
  .brochure-spread {
    position: relative;
    width: 1200px;
    height: 802px;
    background: var(--paper);
  }
  .spread-frame {
    position: absolute;
    left: 0; top: 0;
    width: 1190px;
    height: 795px;
    border: 1px solid var(--frame);
  }
  .hero-photo {
    position: absolute;
    left: 0; top: 0;
    width: 882px;
    height: 795px;
    background: linear-gradient(
      to bottom,
      var(--sky-deep) 0%,
      var(--sky) 22%,
      var(--stone) 34%,
      #8a6a55 46%,
      var(--foliage) 56%,
      #4a6a3c 64%,
      var(--harbour) 74%,
      #6f6a5e 82%,
      var(--water) 88%,
      #3f4c49 100%
    );
  }
  .photo-grid {
    position: absolute;
    left: 0; top: 0;
    width: 882px;
    height: 795px;
  }
  .tagline-panel {
    position: absolute;
    left: 0;
    top: 480px;
    width: 443px;
    height: 158px;
    background: var(--teal);
    display: flex;
    align-items: center;
    padding-left: 56px;
  }
  .tagline {
    font-family: "Cabin", "Open Sans", sans-serif;
    font-weight: 500;
    font-size: 30px;
    line-height: 42px;
    color: #ffffff;
    letter-spacing: 0.2px;
  }
  .intro-column {
    position: absolute;
    left: 922px;
    top: 179px;
    width: 218px;
    font-family: "Arimo", Arial, sans-serif;
  }
  .intro-lead {
    font-size: 13.3px;
    line-height: 16.2px;
    color: var(--teal-text);
    margin-bottom: 2px;
  }
  .intro-body {
    font-size: 11.4px;
    line-height: 15.1px;
    color: var(--body-text);
  }
</style>
</head>
<body>
<main class="brochure-spread">
  <div class="hero-photo" role="img" aria-label="Photograph of a historic château-style hotel on a green cliff above a harbour with ferries on the river"></div>

  <svg class="photo-grid" viewBox="0 0 882 795" aria-hidden="true">
    <g stroke="var(--grid-line)" stroke-width="1.5">
      <line x1="150" y1="0" x2="150" y2="795"/>
      <line x1="297" y1="0" x2="297" y2="795"/>
      <line x1="443" y1="0" x2="443" y2="795"/>
      <line x1="590" y1="0" x2="590" y2="795"/>
      <line x1="737" y1="0" x2="737" y2="795"/>
      <line x1="0" y1="160" x2="882" y2="160"/>
      <line x1="0" y1="320" x2="882" y2="320"/>
      <line x1="0" y1="480" x2="882" y2="480"/>
      <line x1="0" y1="640" x2="882" y2="640"/>
    </g>
  </svg>

  <div class="tagline-panel">
    <h1 class="tagline">ENJOY YOUR<br>LIFE WITHOUT LIMITS</h1>
  </div>

  <section class="intro-column">
    <p class="intro-lead">LES RÉSIDENCES HORIZON presents a unique residential real estate investment opportunity in Salaberry de Valleyfield, one of the fastest growing real estate markets in Quebec.</p>
    <p class="intro-body">Place Verdier will comprise over 78 units separated in blocks of 6 or 12 units per block.</p>
    <p class="intro-body">This turnkey project will offer the possibility to buy 4 ½ or 5 ½ room floor plans of approximately 1120 square feet to be rented as income properties.</p>
    <p class="intro-body">Rental property can be a solid long term investment. Approximately 25% of all new condos being built in Canada are expected to be rental apartments. Other multi-unit properties – duplexes, triplexes and six-plexes – are also expected to provide housing for renters.</p>
    <p class="intro-body">The location is strategically located with direct access to the new provincial Autoroute 30 in close proximity to schools, services, major hospital and fast growing new industrial areas.</p>
  </section>

  <div class="spread-frame" aria-hidden="true"></div>
</main>
</body>
</html>
```